Flyer für Hersteller von Designertischen
Zielgruppe
Wir bauen Designer Tische, unser Zielgruppe liegt zwischen 35 und 50 Jahren
Aufgabenstellung
Wir legen Wert auf ein minimales Design, gerne in dem Stil unserer Website

```html
<!DOCTYPE html>
<html lang="de">
<head>
<meta charset="utf-8">
<title>Lindqvist Manufaktur – Flyer</title>
<link href="https://fonts.googleapis.com/css2?family=Raleway:wght@300;400;500&display=swap" rel="stylesheet">
<style>
  :root {
    --backdrop: #e9e9ea;
    --paper: #f7f7f7;
    --slate: #6b6a78;
    --ink: #3c3c44;
    --on-slate: #e6e6ec;
    --wall-light: #ecebea;
    --wall-mid: #d9d6d1;
    --wood: #b98a52;
    --steel: #3a3a3c;
  }
  * { box-sizing: border-box; margin: 0; padding: 0; }
  html, body { width: 1200px; height: 900px; overflow: hidden; }
  body {
    background: var(--backdrop);
    font-family: "Raleway", sans-serif;
    color: var(--ink);
    position: relative;
  }
  .flyer-side {
    position: absolute;
    left: 60px;
    width: 1080px;
    height: 360px;
    display: flex;
    background: var(--paper);
    box-shadow: 0 2px 6px rgba(0,0,0,.08);
  }
  .flyer-side--outer { top: 50px; }
  .flyer-side--inner { top: 490px; }
  .panel { position: relative; height: 100%; }
  .panel--text { background: var(--paper); padding: 70px 22px 20px; text-align: right; }
  .panel--slate { background: var(--slate); color: var(--on-slate); padding: 70px 36px 20px; }
  .panel-title { font-weight: 400; font-size: 14px; margin-bottom: 12px; }
  .panel-copy { font-weight: 300; font-size: 9.5px; line-height: 1.6; }
  .photo { height: 100%; }
  .photo--wall-wood { background: linear-gradient(160deg, var(--wall-light) 0%, var(--wall-mid) 70%, #c9b79c 100%); }
  .photo--table-bench { background: linear-gradient(170deg, #e7e7e9 0%, #d8d3cc 55%, #b48656 75%, #ddd9d4 100%); }
  .photo--table-steel { background: linear-gradient(165deg, #e9e8e6 0%, #cfc3b0 40%, #7a6f62 70%, #dcdad6 100%); }
  .photo--portrait { background: linear-gradient(180deg, #4a4a4a 0%, #8a8a8a 55%, #bdbdbd 100%); }
  .slate-photo-wrap { display: flex; flex-direction: column; padding: 0; }
  .slate-photo-wrap .slate-text { padding: 36px 36px 10px; }
  .slate-photo-wrap .photo { height: 150px; width: 65%; }
  .cover-claim {
    position: absolute;
    right: 34px;
    top: 130px;
    color: #fff;
    font-weight: 300;
    font-size: 26px;
    line-height: 1.15;
    text-align: right;
  }
  .brand {
    position: absolute;
    right: 26px;
    top: 20px;
    display: flex;
    align-items: center;
    gap: 8px;
    font-weight: 400;
    font-size: 12px;
    color: var(--ink);
  }
  .brand-dot { width: 12px; height: 12px; border: 1px solid var(--ink); border-radius: 50%; }
  .contact { text-align: left; padding: 150px 30px 20px; }
  .contact .panel-copy { font-size: 10px; }
</style>
</head>
<body>

<section class="flyer-side flyer-side--outer">
  <div class="panel" style="width:150px">
    <div class="photo photo--wall-wood" role="img" aria-label="Tisch mit Holzplatte und schwarzem X-Gestell aus Stahl"></div>
  </div>
  <div class="panel panel--text" style="width:210px">
    <h2 class="panel-title">Unsere Vision</h2>
    <p class="panel-copy">Unsere Vision bei der Lindqvist Manufaktur ist es, einen Beitrag zu nachhaltigem Wohnen zu leisten. Wir möchten Möbel herstellen, die nicht nur hohe Qualität bieten, sondern auch Geschichten erzählen. Jedes Stück verbindet Handwerk, Design und Material zu einem Ort, an dem Menschen gerne zusammenkommen.</p>
  </div>
  <div class="panel panel--slate" style="width:330px">
    <h2 class="panel-title">Werte der Lindqvist Manufaktur</h2>
    <p class="panel-copy">Unsere Werte bilden das Fundament der Lindqvist Manufaktur. Wir arbeiten mit regionalen Hölzern, ehrlichem Stahl und viel Sorgfalt. Jeder Tisch entsteht in Handarbeit und wird auf seine Besitzer abgestimmt. Wir legen Wert auf langlebige Verbindungen, klare Formen und einen respektvollen Umgang mit der Natur. So entstehen Möbel, die über Generationen Freude bereiten und mit jeder Mahlzeit, jedem Gespräch und jedem Abend eine neue Geschichte schreiben.</p>
  </div>
  <div class="panel" style="width:390px">
    <div class="photo photo--table-bench" role="img" aria-label="Massivholzbank mit rostigen Stahlkufen vor heller Wand"></div>
    <div class="brand"><span class="brand-dot"></span>Lindqvist</div>
    <p class="cover-claim">Möbel die<br>Geschichten<br>erzählen</p>
  </div>
</section>

<section class="flyer-side flyer-side--inner">
  <div class="panel" style="width:160px">
    <div class="photo photo--wall-wood" role="img" aria-label="Holztisch mit filigranem Stahlgestell"></div>
  </div>
  <div class="panel panel--text" style="width:210px">
    <h2 class="panel-title">Gemeinsame Planung</h2>
    <p class="panel-copy">Gemeinsam mit dir gestalten wir dein individuelles Möbelstück. In einem persönlichen Gespräch erfassen wir deine Vorstellungen und Anforderungen. Basierend darauf entwerfen wir einen detaillierten Plan, der deinem Raum und Stil entspricht. Dabei berücksichtigen wir Material, Größe und Nutzung. Unser Ziel ist ein Tisch, der deine Erwartungen übertrifft.</p>
  </div>
  <div class="panel panel--slate slate-photo-wrap" style="width:280px">
    <div class="slate-text">
      <h2 class="panel-title">Über mich</h2>
      <p class="panel-copy">Ich bin Jonas Lindqvist und Gründer der Lindqvist Manufaktur. Seit vielen Jahren arbeite ich mit Holz und Stahl. In meiner Werkstatt verbinde ich traditionelles Handwerk mit modernem Design. Jedes Möbelstück ist ein Unikat, das mit Geduld und Leidenschaft entsteht und Charakter zeigt.</p>
    </div>
    <div class="photo photo--portrait" style="margin-top:auto" role="img" aria-label="Schwarzweißes Porträt des Gründers in einem Tunnel"></div>
  </div>
  <div class="panel" style="width:200px">
    <div class="photo photo--table-steel" role="img" aria-label="Beistelltisch aus Holz mit Einlage und geknicktem Stahlfuß"></div>
  </div>
  <div class="panel panel--text contact" style="width:230px">
    <h2 class="panel-title">Kontakt</h2>
    <p class="panel-copy">Lindqvist Manufaktur<br>Ahornweg 14<br>72070 Tübingen<br><br>+49 157 0000 4821<br>lindqvist.manufaktur@mailpost.de</p>
  </div>
</section>

</body>
</html>
```